Catering Company Needs a Web Page Design

I already have my logo, and so I'm moving onto the next phase.. the web page design. Platrix is a gourmet catering company based in orlando, fl, set to launch in 2015. I will have a store location to host cooking classes as well.... and will be uploading cooking demo videos to my website weekly. Id like a blog section, and about, a video section, contact form, Services, Menu Samples..... My logo and concept is modern, innovative, and fun! I am targeting middle class to upper middle class women, but i want the site to be super unique.

Industry/Entity Type

Catering

Requirements
Must have
• The front/main page must have the logo... and the lingo ledger's definition of "platrix". I like movement... maybe the top banner can move somehow.. Im not a web designer, so i wont really know until I start seeing some examples. For now I dont have photos of my own cooking, so if you could use stock photos of catering dishes.. I uploaded a transparent logo also, maybe that could be the top banner placed over a scene of expertly plated hordourves...

```html
<!DOCTYPE html>
<html lang="en">
<head>
<meta charset="utf-8">
<title>Platrix – Gourmet Catering</title>
<link rel="stylesheet" href="https://fonts.googleapis.com/css2?family=Bebas+Neue&family=Crimson+Text&family=Droid+Serif:ital@0;1&family=Oswald:wght@400&display=swap">
<style>
:root{
  --brown:#432818;
  --brown-deep:#2f1c10;
  --cream:#efecd6;
  --khaki:#c3bd92;
  --title:#4a2e1a;
  --desc:#a19b7c;
  --green:#6e9a4d;
  --green-dark:#557a38;
  --olive:#9d9574;
  --white:#ffffff;
  --nav:#1d1209;
}
*{margin:0;padding:0;box-sizing:border-box}
html,body{width:1200px;height:984px;overflow:hidden}
body{position:relative;background:var(--white);font-family:Arial,Helvetica,sans-serif}
.hero{position:absolute;left:0;top:0;width:1200px;height:399px;background:linear-gradient(var(--brown-deep),var(--brown) 30px)}
.masthead{position:absolute;left:189px;top:26px;width:1011px;height:54px;background:var(--white);box-shadow:0 1px 3px rgba(0,0,0,.3)}
.brand{position:absolute;left:19px;top:4px;font-family:'Oswald',sans-serif;font-size:34px;color:var(--brown);letter-spacing:-1px}
.main-nav{position:absolute;left:466px;top:18px;display:flex;gap:14px;font-family:'Oswald',sans-serif;font-size:12px;font-weight:700;color:var(--nav)}
.hero-photo{position:absolute;left:563px;top:80px;width:448px;height:319px;border-radius:110px 0 0 0/240px 0 0 0;background:radial-gradient(circle at 60% 45%,#8fa25a 0,#6f8a3c 35%,#c8c9a6 70%,#efefe8 100%)}
.hero-copy{position:absolute;left:204px;top:140px;width:320px;color:var(--white)}
.hero-copy h1{font-family:'Bebas Neue',sans-serif;font-weight:400;font-size:38px;line-height:41px}
.hero-copy p{margin-top:8px;font-size:12px;font-weight:700;line-height:15.5px}
.cta{position:absolute;left:206px;top:303px;width:211px;height:29px;border-radius:15px;background:linear-gradient(var(--green),var(--green-dark));border:1px solid #8fb46c;color:var(--white);font-family:'Crimson Text',serif;font-size:15px;text-align:center;line-height:27px}
.slider-tab{position:absolute;left:542px;top:373px;width:121px;height:30px;background:linear-gradient(#f4f2e3,#fff);border-radius:6px 6px 0 0;display:flex;justify-content:center;gap:4px;padding-top:8px}
.dot{width:12px;height:12px;border-radius:50%;background:#ddd9bb;border:1px solid #c9c4a0}
.dot.active{background:#4a3a22}
.definition{position:absolute;left:0;top:399px;width:1200px;height:107px;background:linear-gradient(#fff,#f4f3ed);border-bottom:1px solid #ddd9c8;text-align:center}
.definition p{margin-top:24px;font-family:'Crimson Text',serif;font-size:22px;color:#6a4a2c}
.rating{position:absolute;left:570px;top:79px}
.features{position:absolute;left:0;top:507px;width:1200px;height:354px;background:var(--cream)}
.col{position:absolute;top:48px}
.col h2{font-family:'Bebas Neue',sans-serif;font-weight:400;font-size:20px;color:var(--khaki);margin-bottom:12px}
.dish{display:flex;gap:11px;height:70px}
.thumb{width:57px;height:57px;border:4px solid #fff;box-shadow:0 0 2px rgba(0,0,0,.3)}
.dish h3{font-family:'Bebas Neue',sans-serif;font-weight:400;font-size:19px;color:var(--title);margin-top:2px}
.dish p{font-family:'Droid Serif',serif;font-style:italic;font-size:10.5px;line-height:15px;color:var(--desc);width:170px}
.video{position:relative;width:222px;height:155px;border:5px solid #fff;box-shadow:0 0 2px rgba(0,0,0,.3);background:linear-gradient(#6a5444,#3b2c22)}
.duration{position:absolute;right:0;bottom:0;width:64px;height:16px;background:#000;color:#fff;font-size:9px;font-weight:700;display:flex;align-items:center;gap:8px;padding-left:10px}
.testimonial{position:relative;width:220px;height:202px;background:#fff;border:1px solid #e2dfcc;border-radius:5px;padding:12px 16px;box-shadow:0 8px 6px -4px rgba(0,0,0,.25)}
.avatar{float:left;width:58px;height:58px;border:4px solid #fff;box-shadow:0 0 2px rgba(0,0,0,.3);background:#9a6a45;margin-right:12px}
.testimonial h3{font-family:'Bebas Neue',sans-serif;font-weight:400;font-size:19px;color:var(--title);margin-top:2px}
.testimonial p{font-family:'Droid Serif',serif;font-style:italic;font-size:10.5px;line-height:17px;color:var(--desc)}
.browse{position:absolute;left:490px;top:847px;width:220px;height:30px;border-radius:15px;background:linear-gradient(#b4ad8a,var(--olive));border:1px solid #857d5d;color:#fff;font-family:'Crimson Text',serif;font-size:15px;text-align:center;line-height:28px;z-index:2}
.footer{position:absolute;left:0;top:861px;width:1200px;height:123px;background:linear-gradient(#fff,#f3f3ef);border-top:1px solid #d8d4bf}
.footer-nav{position:absolute;left:423px;top:56px;display:flex;gap:13px;font-family:'Crimson Text',serif;font-size:12px;color:var(--nav)}
.footer-nav .current{font-style:italic;color:var(--olive)}
</style>
</head>
<body>
<header class="hero">
  <div class="masthead">
    <div class="brand">platrix</div>
    <nav class="main-nav"><span>HOME</span><span>CONTACT</span><span>MENU</span><span>VIDEOS</span><span>BLOG</span><span>SERVICES</span><span>REVIEWS</span></nav>
  </div>
  <div class="hero-photo" role="img" aria-label="Plated zucchini noodles with cherry tomatoes and pine nuts"></div>
  <div class="hero-copy">
    <h1>DELICIOUS FOOD THAT<br>YOU EAT AT HOME</h1>
    <p>Fusce nunc diam, suscipit a iaculis ac, tristique ac erat. Nunc eros lacus, placerat non ornare et, dignissim ut ligula. Duis sed neque et velit rutrum rutrum ut nec tellus. Nulla facilisi. Nullam sed leo fringilla elit volutpat</p>
  </div>
  <div class="cta">Button’s Text Goes Right Here</div>
  <div class="slider-tab"><span class="dot"></span><span class="dot"></span><span class="dot active"></span><span class="dot"></span><span class="dot"></span><span class="dot"></span></div>
</header>

<section class="definition">
  <p>Platrix: Those who are overly zealous and enthusiastic about eating, cooking, and fine dining.</p>
  <svg class="rating" width="60" height="12" viewBox="0 0 60 12" fill="none" stroke="#9a9278" stroke-width="0.8">
    <g id="star"><polygon points="6,1 7.4,4.4 11,4.6 8.2,6.9 9.1,10.5 6,8.5 2.9,10.5 3.8,6.9 1,4.6 4.6,4.4"/></g>
    <use href="#star" x="12"/><use href="#star" x="24"/><use href="#star" x="36"/><use href="#star" x="48"/>
  </svg>
</section>

<main class="features">
  <div class="col" style="left:189px">
    <h2>CHEF’S RECOMMENDATIONS</h2>
    <div class="dish"><div class="thumb" role="img" aria-label="Garnished deviled egg" style="background:#b9c98a"></div><div><h3>Food Title Goes here</h3><p>Description of the food goes right over here yes it does</p></div></div>
    <div class="dish"><div class="thumb" role="img" aria-label="Baked savory muffins" style="background:#c8a060"></div><div><h3>Food Title Goes here</h3><p>Description of the food goes right over here yes it does</p></div></div>
    <div class="dish"><div class="thumb" role="img" aria-label="Caprese skewers" style="background:#7a4a3a"></div><div><h3>Food Title Goes here</h3><p>Description of the food goes right over here yes it does</p></div></div>
  </div>
  <div class="col" style="left:489px">
    <h2>LATEST VIDEOS</h2>
    <div class="video" role="img" aria-label="Cooking demo video of meat on a grill">
      <div class="duration"><svg width="8" height="8" viewBox="0 0 8 8"><polygon points="0,0 8,4 0,8" fill="#fff"/></svg>3:21</div>
    </div>
  </div>
  <div class="col" style="left:789px">
    <h2>CUSTOMER TESTIMONIALS</h2>
    <div class="testimonial">
      <div class="avatar" role="img" aria-label="Customer portrait"></div>
      <h3>Dylan Marsh</h3>
      <p>“In justo nibh, congue nec dapibus ac, placerat</p>
      <p style="clear:both;margin-top:4px">In justo nibh, congue nec dapibus ac, placerat eget sem. Nunc consequat felis non elit ultricies in varius massa laoreet. Aenean lectus nisl, ellentesque in fermentum sit amet, convallis a lorem condimentum mollis augue.”</p>
      <svg style="position:absolute;left:172px;bottom:-18px" width="20" height="18" viewBox="0 0 20 18"><polygon points="0,0 20,0 20,18" fill="#fff"/></svg>
    </div>
  </div>
</main>

<div class="browse">Click Here To Browse The Menu</div>

<footer class="footer">
  <nav class="footer-nav"><span class="current">HOME</span><span>CONTACT</span><span>MENU</span><span>VIDEOS</span><span>BLOG</span><span>SERVICES</span><span>REVIEWS</span></nav>
</footer>
</body>
</html>
```